Flyer for outback tour company

Trifold flyer with a page for each tour that we offer (4 different tours) as well as a front page and a contact page.

Front page: Kestrel Treks logo + an overview of the tours on offer:
- Grand Circuit of the Village and Ridgelands
- Opalvale Showcase Tour
- Twilight Ridgelands Tour
- Subsurface Gemhunt (prospecting) Tour.

Page 2-5: description of each tour with pricing/duration.

Last page (back of brochure): contact details.
Ph: 0488 217 654
E-mail: kestreltreksoz@mailbox-example.net
Online bookings: www.kestreltreksoz-example.com.au.
Tours can also be booked directly through the reception at the Harlow Ridge Desert Lodge and the Clay Nest Inn. Please include the logos for Harlow Ridge and Clay Nest on the last page.

Target Market(s)

Travellers/tourists

Industry/Entity Type

Tourism/tour company

Font styles to use
Sans Serif

Requirements
Must have
• In regards to the pictures… the picture with the tour guide shining the torch should be on the page with the Gemhunt Tour. The other pictures of the cave tunnels should only be on the premium tour/Gemhunt Tour or front/back page.

```html
<!DOCTYPE html>
<html lang="en">
<head>
<meta charset="utf-8">
<title>Kestrel Treks – Trifold Flyer</title>
<link rel="stylesheet" href="https://fonts.googleapis.com/css2?family=Montserrat:ital,wght@0,400;0,500;0,600;0,700;0,800;1,400&display=swap">
<style>
  :root {
    --rust: #c44b2a;
    --rust-dark: #a63c20;
    --charcoal: #2c2a29;
    --ink: #1f1f1f;
    --paper: #f4f4f3;
    --mist: #e2e2e1;
    --stage: #e9e9e9;
    --white: #ffffff;
  }
  * { box-sizing: border-box; margin: 0; padding: 0; }
  html, body { width: 1200px; height: 800px; overflow: hidden; }
  body {
    background: var(--stage);
    font-family: "Montserrat", Arial, sans-serif;
    color: var(--ink);
    position: relative;
  }
  .sheet {
    position: absolute;
    left: 20px;
    width: 1160px;
    height: 380px;
    display: flex;
    box-shadow: 0 4px 14px rgba(0,0,0,.12);
  }
  .sheet--inside { top: 12px; }
  .sheet--outside { top: 408px; }
  .panel {
    position: relative;
    width: 386.67px;
    height: 100%;
    overflow: hidden;
  }
  .panel--mist { background: var(--mist); }
  .panel--paper { background: var(--paper); }
  .panel--rust { background: var(--rust); color: var(--white); }
  .panel--charcoal { background: var(--charcoal); color: var(--white); }

  .photo { position: absolute; left: 0; width: 100%; }
  .photo__wave { position: absolute; left: 0; width: 100%; }

  .photo--canyon-arch { top: 0; height: 150px;
    background: linear-gradient(180deg, #6f8cb3 0%, #a9b9c9 55%, #c89a72 80%, #9c6a45 100%); }
  .photo--painted-hills { bottom: 0; height: 128px;
    background: linear-gradient(180deg, #2f6fb5 0%, #6ea3d3 38%, #d9b28a 62%, #b8703c 100%); }
  .photo--tunnel-guide { bottom: 0; height: 130px;
    background: linear-gradient(135deg, #4c4742 0%, #8d8a86 45%, #5a4333 100%); }
  .photo--sunset-glasses { top: 0; height: 215px;
    background: linear-gradient(180deg, #8fa2b8 0%, #d7b08a 40%, #b8693b 70%, #5a3a2c 100%); }

  .copy { position: absolute; left: 0; width: 100%; }
  .heading {
    font-weight: 800;
    text-transform: uppercase;
    line-height: 1.18;
    letter-spacing: .2px;
  }
  .heading .accent { color: var(--rust); }
  .panel--rust .heading .accent { color: var(--white); }
  .rule { display: block; width: 30px; height: 3px; background: var(--rust); margin: 6px 0 8px; }
  .panel--rust .rule { background: var(--white); margin: 4px auto 6px; }
  .meta { font-weight: 600; font-size: 10.5px; line-height: 1.45; }
  .body { font-size: 9.6px; line-height: 1.4; }

  /* Grand circuit */
  .grand { top: 160px; padding: 0 26px; }
  .grand .heading { font-size: 14.5px; }
  .grand .meta { margin-bottom: 6px; }

  /* Includes / Opalvale */
  .includes { top: 0; padding: 14px 18px; text-align: center; }
  .includes .heading { font-size: 12px; }
  .includes .list { list-style: none; font-size: 9px; line-height: 1.32; }
  .includes .block + .block { margin-top: 8px; }
  .includes .meta { font-size: 9.4px; line-height: 1.35; }
  .includes .body { font-size: 9px; line-height: 1.32; margin: 3px 0 3px; }

  /* Twilight */
  .twilight { top: 0; padding: 22px 26px 0; }
  .twilight .heading { font-size: 14px; }
  .twilight .heading .plain { color: var(--ink); }
  .twilight .meta { font-size: 10px; }
  .twilight .body { margin-top: 4px; }
  .subhead { font-weight: 800; font-size: 9.6px; text-transform: uppercase; margin-top: 8px; }
  .subhead + .rule { width: 24px; height: 2px; margin: 3px 0 5px; }

  .ticks { list-style: none; }
  .ticks li { display: flex; align-items: flex-start; gap: 6px; font-size: 9.6px; line-height: 1.35; margin-bottom: 2px; }
  .ticks svg { flex: 0 0 10px; margin-top: 2px; }

  /* Gemhunt */
  .gemhunt { top: 0; padding: 24px 26px 0; }
  .gemhunt .heading { font-size: 13.5px; }
  .gemhunt .meta { font-size: 10px; }
  .gemhunt .body + .body { margin-top: 6px; }
  .gemhunt .body { margin-top: 6px; }

  /* Contact */
  .contact { top: 0; height: 100%; padding: 26px 0 0; text-align: center; }
  .contact .heading { font-size: 19px; }
  .contact .rule { margin: 5px auto 12px; }
  .contact-item { font-size: 10.5px; font-weight: 500; margin: 5px 0 12px; }
  .icon-badge { display: block; margin: 0 auto; }
  .booking-band {
    background: var(--rust); color: var(--white);
    font-weight: 800; font-size: 13px; text-transform: uppercase;
    padding: 6px 0; margin: 0 22px;
  }
  .web { font-size: 10.5px; font-weight: 500; margin: 9px 0 6px; }
  .contact .body { padding: 0 44px; font-size: 9.6px; }
  .partners { display: flex; justify-content: center; align-items: center; gap: 14px; margin-top: 14px; }
  .partner-name { display: flex; align-items: center; gap: 6px; font-weight: 700; font-size: 12px; color: var(--rust); }
  .partner-name .mark { width: 14px; height: 14px; background: var(--rust); }
  .partners--minor { margin-top: 10px; gap: 18px; }
  .badge { width: 34px; height: 22px; background: #bfbfbe; }
  .badge--round { width: 26px; height: 26px; border-radius: 50%; }

  /* Front */
  .front-logo {
    position: absolute; left: 50%; top: 160px; transform: translateX(-50%);
    width: 130px; height: 130px; border-radius: 50%;
    background: var(--mist);
    display: flex; align-items: center; justify-content: center; text-align: center;
    font-weight: 800; font-size: 17px; color: var(--charcoal); line-height: 1.1;
    z-index: 2;
  }
  .front-dark { position: absolute; left: 0; bottom: 0; width: 100%; height: 165px; background: var(--charcoal); }
  .front-tours { position: absolute; left: 0; bottom: 18px; width: 100%; padding: 0 32px; color: var(--white); z-index: 2; }
  .front-tours .ticks li { font-size: 10.5px; margin-bottom: 5px; }
</style>
</head>
<body>

<!-- Inside spread -->
<section class="sheet sheet--inside">

  <article class="panel panel--mist">
    <div class="photo photo--canyon-arch" role="img" aria-label="Photo: tour 4WD vehicle framed by a sandstone rock arch in the desert"></div>
    <svg class="photo__wave" style="top:110px" width="387" height="50" viewBox="0 0 387 50" aria-hidden="true">
      <path d="M0 0 C60 45 170 20 260 30 C320 36 360 30 387 10 L387 50 L0 50 Z" fill="var(--rust)"/>
      <path d="M0 10 C60 52 170 28 260 38 C320 44 360 38 387 18 L387 50 L0 50 Z" fill="var(--mist)"/>
    </svg>
    <div class="copy grand">
      <h2 class="heading">Grand Circuit<br><span class="accent">of the Village and</span><br>Ridgelands</h2>
      <span class="rule"></span>
      <p class="meta">$99 adults/$75 children<br>Duration: approx. 5 hours<br>1pm start</p>
      <p class="body">This tour is designed for those who want a more personal, authentic experience. Smaller groups, bigger experience. Sit back and relax in our spacious air-conditioned 4wd vehicle as we take you places in and around Opalvale that the others can't.</p>
    </div>
  </article>

  <article class="panel panel--rust">
    <div class="copy includes">
      <div class="block">
        <h2 class="heading">The Tour Includes</h2>
        <span class="rule"></span>
        <ul class="list">
          <li>The Old Quarry Underground Chapel</li>
          <li>Modern Underground Home (dugout).</li>
          <li>The Lunar Flats</li>
          <li>The Dingo Fence</li>
          <li>The Ridgelands.</li>
          <li>Underground Mine Tour at our private claim in the opal fields (exclusive to Kestrel Treks)</li>
        </ul>
      </div>
      <div class="block">
        <h2 class="heading">Opalvale<br>Showcase Tour</h2>
        <span class="rule"></span>
        <p class="meta">$85 adults/ $59 children<br>Family rate<br>(2 adults and 2 children): $270<br>Duration approx: 5 hours</p>
        <p class="body">A tour that gives you a great insight and introduction into this unique outback town and the surrounding area. Highlights include</p>
        <ul class="list">
          <li>Glimmerstone Opal Mine &amp; Museum</li>
          <li>The Old Quarry Underground Chapel</li>
          <li>The dingo fence</li>
          <li>The Lunar Flats</li>
          <li>The Ridgelands</li>
        </ul>
      </div>
    </div>
  </article>

  <article class="panel panel--paper">
    <div class="copy twilight">
      <h2 class="heading"><span class="accent">Twilight Ridgelands</span><br><span class="plain">Tour: $60</span></h2>
      <span class="rule"></span>
      <p class="meta">Duration approx. 3.5 hours<br>Departs 3 hours before sunset</p>
      <p class="body">A perfect way to end the day. Take in the spectacular views of the colourful Ridgelands. Watch the sun go down across the desert horizon, while enjoying a hot beverage (tea, coffee, hot chocolate) in one hand and a home-made scone in the other.</p>
      <p class="subhead">This tour includes</p>
      <span class="rule"></span>
      <ul class="ticks">
        <li><svg width="10" height="10" viewBox="0 0 10 10" aria-hidden="true"><circle cx="5" cy="5" r="4.3" fill="none" stroke="var(--rust)" stroke-width="1"/><path d="M3 5.1 L4.5 6.5 L7 3.6" fill="none" stroke="var(--rust)" stroke-width="1.1"/></svg>The Dingo fence</li>
        <li><svg width="10" height="10" viewBox="0 0 10 10" aria-hidden="true"><circle cx="5" cy="5" r="4.3" fill="none" stroke="var(--rust)" stroke-width="1"/><path d="M3 5.1 L4.5 6.5 L7 3.6" fill="none" stroke="var(--rust)" stroke-width="1.1"/></svg>The Lunar Flats</li>
        <li><svg width="10" height="10" viewBox="0 0 10 10" aria-hidden="true"><circle cx="5" cy="5" r="4.3" fill="none" stroke="var(--rust)" stroke-width="1"/><path d="M3 5.1 L4.5 6.5 L7 3.6" fill="none" stroke="var(--rust)" stroke-width="1.1"/></svg>The Ridgelands</li>
      </ul>
    </div>
    <div class="photo photo--painted-hills" role="img" aria-label="Photo: colourful painted desert hills under a blue sky"></div>
    <svg class="photo__wave" style="bottom:98px" width="387" height="50" viewBox="0 0 387 50" aria-hidden="true">
      <path d="M0 0 L387 0 L387 44 C330 10 260 22 180 20 C100 18 40 30 0 50 Z" fill="var(--rust)"/>
      <path d="M0 0 L387 0 L387 36 C330 2 260 14 180 12 C100 10 40 22 0 42 Z" fill="var(--paper)"/>
    </svg>
  </article>

</section>

<!-- Outside spread -->
<section class="sheet sheet--outside">

  <article class="panel panel--charcoal">
    <div class="copy gemhunt">
      <h2 class="heading"><span class="accent">Subsurface Gemhunt</span><br>(Prospecting) Tour: $50</h2>
      <span class="rule"></span>
      <p class="meta">Duration approx. 2 hours<br>9.30am start</p>
      <p class="body">This tour is ideal for those who don't mind getting down and dirty whilst searching for their own opals.</p>
      <p class="body">Exclusive to Kestrel Treks, this impressive opal mine has extracted hundreds of thousands of dollars worth of opal.</p>
      <p class="body">After a quick introduction to gemhunting, you will be handed a blacklight, sieve and shovel to explore the tailings in the hopes of finding your own piece of opal to take home with you. A truly unique experience.</p>
    </div>
    <div class="photo photo--tunnel-guide" role="img" aria-label="Photo: tour guide in a hat shining a torch down an underground mine tunnel"></div>
    <svg class="photo__wave" style="bottom:100px" width="387" height="50" viewBox="0 0 387 50" aria-hidden="true">
      <path d="M0 0 L387 0 L387 50 C340 20 270 14 180 18 C100 21 40 16 0 24 Z" fill="var(--rust)"/>
      <path d="M0 0 L387 0 L387 42 C340 12 270 6 180 10 C100 13 40 8 0 16 Z" fill="var(--charcoal)"/>
    </svg>
  </article>

  <article class="panel panel--paper">
    <div class="copy contact">
      <h2 class="heading">Visit us at</h2>
      <span class="rule"></span>
      <svg class="icon-badge" width="24" height="24" viewBox="0 0 24 24" aria-hidden="true"><circle cx="12" cy="12" r="12" fill="var(--rust)"/><rect x="8.5" y="5.5" width="7" height="13" rx="1.5" fill="none" stroke="#fff" stroke-width="1.5"/><circle cx="12" cy="16" r=".9" fill="#fff"/></svg>
      <p class="contact-item">0488 217 654</p>
      <svg class="icon-badge" width="24" height="24" viewBox="0 0 24 24" aria-hidden="true"><circle cx="12" cy="12" r="12" fill="var(--rust)"/><rect x="6" y="8" width="12" height="8.5" rx="1" fill="none" stroke="#fff" stroke-width="1.4"/><path d="M6.3 8.5 L12 13 L17.7 8.5" fill="none" stroke="#fff" stroke-width="1.4"/></svg>
      <p class="contact-item">kestreltreksoz@mailbox-example.net</p>
      <p class="booking-band">Online bookings</p>
      <p class="web">www.kestreltreksoz-example.com.au</p>
      <p class="body">Tours can also be booked directly through the reception at the Harlow Ridge Desert Lodge and the Clay Nest Inn.</p>
      <div class="partners">
        <span class="partner-name"><span class="mark"></span>Clay Nest</span>
        <span class="partner-name"><span class="mark"></span>Harlow Ridge</span>
      </div>
      <div class="partners partners--minor">
        <span class="badge" aria-label="Partner badge"></span>
        <span class="badge badge--round" aria-label="Partner badge"></span>
      </div>
    </div>
  </article>

  <article class="panel panel--charcoal">
    <div class="photo photo--sunset-glasses" role="img" aria-label="Photo: two glasses of sparkling wine on a gravel ridge overlooking the desert at sunset"></div>
    <svg class="photo__wave" style="top:195px" width="387" height="40" viewBox="0 0 387 40" aria-hidden="true">
      <path d="M0 20 C90 0 200 0 300 10 C340 14 370 22 387 40 L387 40 L0 40 Z" fill="var(--rust)"/>
      <path d="M0 26 C90 8 200 8 300 18 C340 22 370 30 387 40 L0 40 Z" fill="var(--charcoal)"/>
    </svg>
    <div class="front-logo">Kestrel<br>Treks</div>
    <div class="front-tours">
      <ul class="ticks">
        <li><svg width="10" height="10" viewBox="0 0 10 10" aria-hidden="true"><circle cx="5" cy="5" r="4.3" fill="none" stroke="var(--rust)" stroke-width="1"/><path d="M3 5.1 L4.5 6.5 L7 3.6" fill="none" stroke="var(--rust)" stroke-width="1.1"/></svg>Grand Circuit of the Village and Ridgelands</li>
        <li><svg width="10" height="10" viewBox="0 0 10 10" aria-hidden="true"><circle cx="5" cy="5" r="4.3" fill="none" stroke="var(--rust)" stroke-width="1"/><path d="M3 5.1 L4.5 6.5 L7 3.6" fill="none" stroke="var(--rust)" stroke-width="1.1"/></svg>Opalvale Showcase Tour</li>
        <li><svg width="10" height="10" viewBox="0 0 10 10" aria-hidden="true"><circle cx="5" cy="5" r="4.3" fill="none" stroke="var(--rust)" stroke-width="1"/><path d="M3 5.1 L4.5 6.5 L7 3.6" fill="none" stroke="var(--rust)" stroke-width="1.1"/></svg>Twilight Ridgelands Tour</li>
        <li><svg width="10" height="10" viewBox="0 0 10 10" aria-hidden="true"><circle cx="5" cy="5" r="4.3" fill="none" stroke="var(--rust)" stroke-width="1"/><path d="M3 5.1 L4.5 6.5 L7 3.6" fill="none" stroke="var(--rust)" stroke-width="1.1"/></svg>Subsurface Gemhunt (prospecting) Tour.</li>
      </ul>
    </div>
  </article>

</section>

</body>
</html>
```